Wade Merriton Professional Coaching

I would like a website with a mountain theme geared towards professional executives reaching higher peaks and goals. This is a 3 page website with brand essence information on the opening page, the coaching process on a second page and "about me" and lead capture form on a third page

Target Market(s)

C-Level audience, involved in tech, government, manufacturing, and transportation type of corporations

Coding

Number of Pages Required

3 page

Font styles to use
Sans Serif

Colors
a7a7a7
1b1b1b
e8e8e8
3176b5
abd036
0355a3

Requirements
Must have
• Looking for a user friendly site that I can manage/update going forward. Must have:
• 1. "Is coaching right for you?" - page 1
• 2. "Our Process" page 2 - I will describe how we approach coaching
• 3. "Contact us" page 3 where I can capture contact information from potential clients
• 4. Clean and professional with more modern font
• 5. Links to personal social media sites
• 6. Ability to upload/download .pdf documents as resources
• 7. Ability to add on new pages in the future (such as a blog page)
Nice to have
• I want a place to store articles I write or use.
• LinkedIn or Twitter Feed
Should not have
• Not fluffy or too 'zen' like personal life coaches tend to present.

```html
<!DOCTYPE html>
<html lang="en">
<head>
<meta charset="utf-8">
<title>Wade Merriton Professional Coaching</title>
<link href="https://fonts.googleapis.com/css2?family=Poppins:wght@300;400;500;600;700&display=swap" rel="stylesheet">
<style>
:root{
  --blue:#0355a3;
  --blue-mid:#3176b5;
  --green:#abd036;
  --ink:#1b1b1b;
  --grey:#a7a7a7;
  --light:#e8e8e8;
  --white:#ffffff;
}
*{box-sizing:border-box;margin:0;padding:0}
html,body{width:1200px;height:3072px;overflow:hidden}
body{font-family:'Poppins',sans-serif;color:var(--ink);background:var(--white);position:relative}
p{color:var(--grey);font-size:11px;line-height:20px}

/* Nav */
.site-nav{position:absolute;top:0;left:0;width:1200px;height:80px;z-index:5}
.nav-link{position:absolute;top:0;height:58px;line-height:50px;font-size:11px;color:#6b6b6b;text-decoration:none}
.nav-link.active{background:var(--blue);color:var(--white);padding:0 12px;height:88px;line-height:48px}
.brand{position:absolute;left:518px;top:14px;width:164px;text-align:center}
.brand-name{font-size:19px;font-weight:600;color:var(--ink);letter-spacing:.5px;line-height:22px}
.brand-sub{font-size:7px;letter-spacing:2px;color:var(--ink);text-transform:uppercase}
.nav-divider{position:absolute;left:878px;top:40px;width:1px;height:22px;background:var(--light)}
.social-sq{position:absolute;top:44px;width:12px;height:12px}

/* Hero */
.hero{position:absolute;top:0;left:0;width:1200px;height:600px}
.hero-photo{position:absolute;inset:0;background:linear-gradient(180deg,#3c3f45 0%,#5d636c 35%,#8d939b 60%,#50555c 100%)}
.hero-curves{position:absolute;inset:0}
.hero-title{position:absolute;top:256px;width:1200px;text-align:center;color:var(--white);font-size:29px;font-weight:700;letter-spacing:2px}
.hero-text{position:absolute;top:302px;left:310px;width:580px;text-align:center;color:var(--white);font-size:11px;line-height:20px}
.hero-actions{position:absolute;top:358px;left:490px;display:flex;gap:8px}
.btn{display:inline-block;font-size:11px;text-decoration:none;text-align:center}
.btn-green{background:var(--green);color:var(--white);width:106px;height:30px;line-height:30px}
.btn-white{background:var(--white);color:var(--green);width:106px;height:30px;line-height:30px}

/* Section headings */
.section-title{font-size:22px;font-weight:700;letter-spacing:2px;color:var(--ink);text-transform:uppercase}
.section-title .dash{display:inline-block;width:14px;height:3px;background:var(--blue);vertical-align:middle;margin:0 8px}

/* Intro */
.intro{position:absolute;top:640px;left:162px;width:876px;height:540px}
.intro .section-title{position:absolute;top:12px;left:-8px}
.intro-copy{position:absolute;top:66px;left:0;width:455px}
.intro-copy p+p{margin-top:14px}
.btn-outline{position:absolute;top:288px;left:0;width:158px;height:30px;line-height:28px;border:1px solid var(--green);color:var(--green);font-size:11px;text-align:center}
.coach-photo{position:absolute;top:20px;left:500px;width:376px;height:428px;background:linear-gradient(160deg,#6f8c4a 0%,#9fb37a 40%,#2f3e5e 70%,#27324a 100%);box-shadow:0 4px 14px rgba(0,0,0,.2)}
.quote-box{position:absolute;top:360px;left:0;width:575px;height:148px;background:var(--green);padding:30px 45px}
.quote-box p{color:var(--white);font-size:11px;line-height:20px}
.quote-mark{font-weight:700;font-size:18px;vertical-align:-4px}

/* Process */
.process{position:absolute;top:1237px;left:0;width:1200px;height:586px;background:var(--light)}
.process .section-title{position:absolute;top:50px;width:1200px;text-align:center}
.step{position:absolute;width:146px;background:var(--white);padding:38px 14px 14px;box-shadow:0 2px 6px rgba(0,0,0,.08)}
.step::after{content:"";position:absolute;right:-12px;top:0;border-left:12px solid var(--white);border-top:14px solid transparent;border-bottom:14px solid transparent;z-index:2}
.step.low{top:207px;height:286px}
.step.high{top:161px;height:306px;background:var(--green)}
.step.high::after{border-left-color:var(--green)}
.step.high h3,.step.high p,.step.high .read-more{color:var(--white)}
.step h3{font-size:12px;font-weight:700;letter-spacing:.5px;text-transform:uppercase;margin-top:10px;line-height:16px}
.step p{font-size:9.5px;line-height:20px;margin-top:6px}
.step .read-more{display:block;font-size:10px;font-weight:600;color:var(--ink);margin-top:8px}
.step-icon{width:30px;height:30px}
.step-num{position:absolute;width:30px;height:30px;border-radius:50%;background:var(--white);text-align:center;line-height:30px;font-size:16px;font-weight:700}

/* Blog */
.blog{position:absolute;top:1860px;left:162px;width:876px;height:700px}
.blog .section-title{position:absolute;top:18px;width:876px;text-align:center}
.post{position:absolute;display:flex;align-items:flex-end;padding:12px;overflow:hidden}
.post span{position:relative;color:var(--white);font-weight:500}
.post.big span{font-size:16px;line-height:26px;padding:0 10px 14px}
.post.small span{font-size:10px;line-height:13px}
.btn-view{position:absolute;top:648px;left:374px;width:128px;height:30px;line-height:28px;border:1px solid var(--green);color:var(--green);font-size:10px;text-align:center}

/* Contact */
.contact{position:absolute;top:2615px;left:0;width:1200px;height:395px;background:linear-gradient(135deg,#0355a3 0%,#0a5fae 55%,#0b4f98 100%)}
.contact-info{position:absolute;top:46px;left:236px;width:280px;color:var(--white)}
.contact-info .section-title{color:var(--white);font-size:22px}
.contact-info .section-title .dash{background:var(--white);margin-left:0}
.contact-info p{color:var(--white);margin-top:8px;font-size:11px;line-height:16px}
.info-row{display:flex;gap:10px;align-items:flex-start;margin-top:18px;font-size:11px;line-height:15px}
.info-row svg{flex:none}
.info-rule{border-top:1px solid rgba(255,255,255,.3);margin-top:14px}
.contact-social{display:flex;gap:12px;margin-top:16px}
.contact-social span{width:26px;height:26px;display:block}
.contact-form{position:absolute;top:-16px;left:612px;width:351px;height:340px;background:var(--green);padding:18px 22px}
.contact-form h4{color:var(--white);font-size:16px;font-weight:700;letter-spacing:1px}
.contact-form .lead{color:var(--white);font-size:10px;margin:4px 0 12px}
.field{display:flex;align-items:center;gap:8px;background:var(--white);height:30px;margin-bottom:11px;padding:0 8px;font-size:10px;color:var(--grey)}
.field.message{height:74px;align-items:flex-start;padding-top:8px}
.btn-submit{display:inline-block;background:var(--blue);color:var(--white);font-size:10px;font-weight:600;letter-spacing:1px;width:82px;height:30px;line-height:30px;text-align:center}

.site-footer{position:absolute;top:3010px;left:0;width:1200px;height:62px;text-align:center;line-height:62px;font-size:10px;color:var(--grey)}
</style>
</head>
<body>

<section class="hero">
  <div class="hero-photo" role="img" aria-label="Snow-covered mountain range under a grey sky"></div>
  <svg class="hero-curves" width="1200" height="600" viewBox="0 0 1200 600">
    <path d="M0 0 H1200 V80 Q600 50 0 80 Z" fill="#ffffff"/>
    <path d="M0 520 Q600 620 1200 520 V600 H0 Z" fill="#ffffff"/>
    <path d="M0 520 Q600 620 1200 520 V528 Q600 628 0 528 Z" fill="#0355a3"/>
  </svg>
  <h1 class="hero-title">PROFESSIONAL EXECUTIVE COACHING</h1>
  <p class="hero-text">Lorem ipsum dolor sit amet, consectetur adipiscing elit, sed do eiusmod tempor incididunt ut labore et dolore magna aliqua. Ut enim ad minim veniam, quis nostrud exercitation</p>
  <div class="hero-actions">
    <a class="btn btn-green" href="#">Let's Talk</a>
    <a class="btn btn-white" href="#">About Us</a>
  </div>
</section>

<nav class="site-nav">
  <a class="nav-link active" href="#" style="left:162px">Home</a>
  <a class="nav-link" href="#" style="left:238px">Is Coaching Right for You?</a>
  <a class="nav-link" href="#" style="left:420px">Our Process</a>
  <div class="brand">
    <div class="brand-name">WADE MERRITON</div>
    <div class="brand-sub">Professional Coaching</div>
  </div>
  <a class="nav-link" href="#" style="left:720px">Blog</a>
  <a class="nav-link" href="#" style="left:781px">Contact Us</a>
  <span class="nav-divider"></span>
  <span class="social-sq" style="left:916px;background:var(--green)"></span>
  <span class="social-sq" style="left:950px;background:var(--grey)"></span>
</nav>

<section class="intro">
  <h2 class="section-title"><span class="dash"></span>Is Coaching Right for You?</h2>
  <div class="intro-copy">
    <p>Lorem ipsum dolor sit amet, consectetur adipiscing elit, sed do eiusmod tempor incididunt ut labore et dolore magna aliqua. Ut enim ad minim veniam, quis nostrud exercitation ullamco laboris nisi ut aliquip ex ea commodo consequat. Duis aute irure dolor in reprehenderit in voluptate velit esse cillum dolore eu fugiat nulla pariatur. Excepteur sint occaecat cupidatat non proident.</p>
    <p>Sed ut perspiciatis unde omnis iste natus error sit voluptatem accusantium doloremque laudantium, totam rem aperiam, eaque ipsa quae ab illo inventore veritatis et quasi architecto beatae vitae dicta sunt, qui dolorem ipsum quia dolor sit amet, consectetur, adipisci velit, sed quia non numquam.</p>
  </div>
  <a class="btn-outline" href="#">Download Brochure &#8595;</a>
  <div class="coach-photo" role="img" aria-label="Portrait of the coach in a blazer, leaning on a wooden rail outdoors"></div>
  <div class="quote-box">
    <p><span class="quote-mark">&ldquo;</span> Sed ut perspiciatis unde omnis iste natus error sit voluptatem accusantium doloremque laudantium, totam rem aperiam, eaque ipsa quae ab illo inventore veritatis et quasi architecto beatae vitae dicta sunt explicabo Nemo enim ipsam voluptatem quia voluptas sit. <span class="quote-mark">&rdquo;</span></p>
  </div>
</section>

<section class="process">
  <h2 class="section-title"><span class="dash"></span>Our Process<span class="dash"></span></h2>

  <span class="step-num" style="left:220px;top:158px;color:var(--blue)">1</span>
  <article class="step low" style="left:162px">
    <svg class="step-icon" viewBox="0 0 30 30"><circle cx="15" cy="15" r="12" fill="none" stroke="#0355a3" stroke-width="2"/><circle cx="15" cy="15" r="6" fill="none" stroke="#e53935" stroke-width="2"/><circle cx="15" cy="15" r="2" fill="#0355a3"/></svg>
    <h3>Goal-Setting</h3>
    <p>Lorem ipsum dolor sit amet, consect etur adipiscing elit, sed do eiusmod tempor incididunt ut labore et dolore magna aliqua. Ut labore et</p>
    <span class="read-more">Read More</span>
  </article>

  <article class="step high" style="left:308px">
    <svg class="step-icon" viewBox="0 0 30 30"><circle cx="11" cy="11" r="6" fill="none" stroke="#fff" stroke-width="2"/><circle cx="20" cy="19" r="6" fill="none" stroke="#fff" stroke-width="2"/></svg>
    <h3>Assessments</h3>
    <p>Lorem ipsum dolor sit amet, consect etur adipiscing elit, sed do eiusmod tempor incididunt ut labore et dolore magna aliqua. Ut labore et</p>
    <span class="read-more">Read More</span>
  </article>
  <span class="step-num" style="left:364px;top:478px;color:var(--green)">2</span>

  <span class="step-num" style="left:512px;top:158px;color:#e53935">3</span>
  <article class="step low" style="left:454px">
    <svg class="step-icon" viewBox="0 0 30 30"><rect x="5" y="4" width="20" height="22" fill="none" stroke="#e53935" stroke-width="2"/><path d="M9 11h12M9 16h12M9 21h8" stroke="#e53935" stroke-width="2"/></svg>
    <h3>Development Planning</h3>
    <p>Lorem ipsum dolor sit amet, consect etur adipiscing elit, sed do eiusmod tempor incididunt ut labore et dolore magna</p>
    <span class="read-more">Read More</span>
  </article>

  <article class="step high" style="left:600px;background:var(--white)">
    <svg class="step-icon" viewBox="0 0 30 30"><circle cx="8" cy="8" r="4" fill="none" stroke="#f2b632" stroke-width="2"/><circle cx="22" cy="8" r="4" fill="none" stroke="#f2b632" stroke-width="2"/><circle cx="15" cy="22" r="4" fill="none" stroke="#f2b632" stroke-width="2"/><path d="M12 8h6M10 11l3 8M20 11l-3 8" stroke="#f2b632" stroke-width="2"/></svg>
    <h3 style="color:var(--ink)">Implement</h3>
    <p style="color:var(--grey)">Lorem ipsum dolor sit amet, consect etur adipiscing elit, sed do eiusmod tempor incididunt ut labore et dolore magna aliqua. Ut labore et</p>
    <span class="read-more" style="color:var(--ink)">Read More</span>
  </article>
  <span class="step-num" style="left:656px;top:478px;color:#f2b632">4</span>

  <span class="step-num" style="left:804px;top:158px;color:var(--green)">5</span>
  <article class="step low" style="left:746px">
    <svg class="step-icon" viewBox="0 0 30 30"><rect x="5" y="4" width="18" height="22" fill="none" stroke="#6aa84f" stroke-width="2"/><circle cx="17" cy="17" r="5" fill="none" stroke="#6aa84f" stroke-width="2"/><path d="M21 21l5 5" stroke="#6aa84f" stroke-width="2"/></svg>
    <h3>Evaluation</h3>
    <p>Lorem ipsum dolor sit amet, consect etur adipiscing elit, sed do eiusmod tempor incididunt ut labore et dolore magna aliqua. Ut labore et</p>
    <span class="read-more">Read More</span>
  </article>

  <article class="step high" style="left:892px;background:var(--white)">
    <svg class="step-icon" viewBox="0 0 30 30"><rect x="5" y="4" width="20" height="22" fill="none" stroke="#3176b5" stroke-width="2"/><path d="M10 21v-5M15 21v-9M20 21v-7" stroke="#3176b5" stroke-width="2"/></svg>
    <h3 style="color:var(--ink)">Results</h3>
    <p style="color:var(--grey)">Lorem ipsum dolor sit amet, consect etur adipiscing elit, sed do eiusmod tempor incididunt ut labore et dolore magna aliqua. Ut labore et</p>
    <span class="read-more" style="color:var(--ink)">Read More</span>
  </article>
  <span class="step-num" style="left:950px;top:478px;color:var(--blue)">6</span>
</section>

<section class="blog">
  <h2 class="section-title"><span class="dash"></span>Blog Post<span class="dash"></span></h2>
  <a class="post big" href="#" role="img" aria-label="Businesswoman presenting in a dark room" style="left:0;top:84px;width:426px;height:336px;background:linear-gradient(135deg,#2b2b2b,#3a3a3a 60%,#4a4a40)"><span>Lorem ipsum dolor sit amet, consectetur adipiscing elit, sed do eiusmod</span></a>
  <a class="post small" href="#" role="img" aria-label="Excited woman raising her hands" style="left:450px;top:84px;width:200px;height:145px;background:linear-gradient(135deg,#c9c9c9,#8d8d8d)"><span>Lorem ipsum dolor sit amet, consectetur adipi</span></a>
  <a class="post small" href="#" role="img" aria-label="Colleagues reviewing a tablet at a desk" style="left:674px;top:84px;width:202px;height:145px;background:linear-gradient(135deg,#9a9a9a,#5c5c5c)"><span>Lorem ipsum dolor sit amet, consectetur adipi</span></a>
  <a class="post big" href="#" role="img" aria-label="Smiling businessman beside a rising arrow graphic" style="left:450px;top:252px;width:426px;height:336px;background:linear-gradient(135deg,#b4b4b4,#7d7d7d 60%,#5f5f5f)"><span>Lorem ipsum dolor sit amet, consectetur adipiscing elit, sed do eiusmod</span></a>
  <a class="post small" href="#" role="img" aria-label="Chalkboard with training related words" style="left:0;top:444px;width:202px;height:144px;background:linear-gradient(135deg,#1f5c8c,#0f3e66)"><span>Lorem ipsum dolor sit amet, consectetur adipi</span></a>
  <a class="post small" href="#" role="img" aria-label="Two business people giving a high five" style="left:224px;top:444px;width:202px;height:144px;background:linear-gradient(135deg,#3a3a3a,#7a6a5a)"><span>Lorem ipsum dolor sit amet, consectetur adipi</span></a>
  <a class="btn-view" href="#">View All Blog Post</a>
</section>

<section class="contact">
  <div class="contact-info">
    <h2 class="section-title"><span class="dash"></span>Contact Us</h2>
    <p>Please complete and submit this form and one of our representatives will reply promptly</p>
    <div class="info-row">
      <svg width="14" height="18" viewBox="0 0 14 18"><path d="M7 1a6 6 0 0 0-6 6c0 4 6 10 6 10s6-6 6-10a6 6 0 0 0-6-6z" fill="none" stroke="#fff" stroke-width="1.5"/><circle cx="7" cy="7" r="2" fill="#fff"/></svg>
      <span>Sed ut perspiciatis unde omnis iste<br>natus error sit voluptatem</span>
    </div>
    <div class="info-rule"></div>
    <div class="info-row">
      <svg width="14" height="14" viewBox="0 0 14 14"><path d="M3 1l2 3-1.5 1.5a8 8 0 0 0 5 5L10 9l3 2-1 2c-6 0-11-5-11-11z" fill="none" stroke="#fff" stroke-width="1.3"/></svg>
      <span>+123 456 789</span>
    </div>
    <div class="info-row" style="margin-top:12px">
      <svg width="14" height="12" viewBox="0 0 14 12"><rect x="1" y="1" width="12" height="10" fill="none" stroke="#fff" stroke-width="1.3"/><path d="M1 1l6 5 6-5" fill="none" stroke="#fff" stroke-width="1.3"/></svg>
      <span>hello@merritonsummit.com</span>
    </div>
    <div class="info-rule"></div>
    <div class="contact-social">
      <span style="background:var(--green)"></span>
      <span style="border:2px solid var(--white)"></span>
    </div>
  </div>

  <form class="contact-form">
    <h4>HELLO</h4>
    <div class="lead">Feel free to drop us a line below!</div>
    <div class="field">&#9786; Your Name</div>
    <div class="field">&#9993; Your Email</div>
    <div class="field">&#9776; Subject</div>
    <div class="field message">? Message</div>
    <span class="btn-submit">SUBMIT</span>
  </form>
</section>

<footer class="site-footer">&copy; Wade Merriton All rights reserved</footer>

</body>
</html>
```